KRT business cards

I need a Business card design for my self. I am behavior analyst owner of a new company based in Miami. We offer Applied Behavior Analysis (ABA) services to individuals with developmental disabilities.

Business

```html
<!DOCTYPE html>
<html lang="en">
<head>
<meta charset="utf-8">
<title>KRT Business Cards</title>
<link rel="stylesheet" href="https://fonts.googleapis.com/css2?family=Cinzel:wght@400&family=Open+Sans:wght@600;700&family=Questrial&display=swap">
<style>
  :root {
    --backdrop: #2b2b2b;
    --leaf-green: #4e9e45;
    --card-white: #f7f7f7;
    --brand-blue: #1d5289;
    --ink: #1a1a1a;
    --text-grey: #222;
    --on-green: #eef6ec;
  }
  * { margin: 0; padding: 0; box-sizing: border-box; }
  html, body { width: 1200px; height: 900px; overflow: hidden; }
  body { background: var(--backdrop); position: relative; font-family: "Questrial", sans-serif; }

  .card { position: absolute; width: 620px; height: 354px; overflow: hidden; box-shadow: 0 10px 30px rgba(0,0,0,.45); }

  /* back of card */
  .card-back { left: 90px; top: 70px; background: var(--leaf-green); }
  .card-back .brand {
    position: absolute; left: 0; right: 0; top: 120px;
    display: flex; align-items: center; justify-content: center; gap: 16px;
  }
  .brand-dot { width: 34px; height: 34px; border-radius: 50%; background: var(--on-green); }
  .brand-name { font-family: "Questrial", sans-serif; font-size: 64px; letter-spacing: 4px; color: var(--brand-blue); line-height: 1; }
  .card-back .tagline {
    position: absolute; left: 0; right: 0; bottom: 46px; text-align: center;
    font-family: "Open Sans", sans-serif; font-weight: 600; font-size: 17px;
    letter-spacing: 4px; color: var(--on-green);
  }

  /* front of card */
  .card-front { left: 490px; top: 476px; background: var(--card-white); }
  .holder { position: absolute; left: 52px; top: 44px; }
  .holder-name { font-family: "Cinzel", serif; font-size: 24px; color: var(--brand-blue); letter-spacing: 1px; line-height: 1.1; }
  .holder-role { font-family: "Open Sans", sans-serif; font-weight: 700; font-size: 12.5px; color: var(--ink); }

  .card-front .brand {
    position: absolute; left: 400px; top: 120px; display: flex; align-items: center; gap: 12px;
  }
  .card-front .brand-dot { background: var(--leaf-green); width: 30px; height: 30px; }
  .card-front .brand-name { font-size: 60px; }

  .icon-tab {
    position: absolute; left: 0; top: 168px; width: 42px; height: 162px;
    background: var(--brand-blue); border-radius: 0 10px 10px 0;
    display: flex; flex-direction: column; justify-content: space-around; align-items: center; padding: 8px 0;
  }
  .icon-tab svg { width: 24px; height: 24px; }

  .contact { position: absolute; left: 72px; top: 176px; list-style: none; font-size: 17px; color: var(--text-grey); }
  .contact li { line-height: 30px; }
  .contact .address { line-height: 22px; margin-top: 4px; }

  .edge-bands { position: absolute; left: 0; bottom: 0; width: 620px; height: 44px; }
</style>
</head>
<body>

  <section class="card card-back">
    <div class="brand">
      <span class="brand-dot"></span>
      <span class="brand-name">KRT</span>
    </div>
    <p class="tagline">APPLIED BEHAVIOR ANALYSIS</p>
  </section>

  <section class="card card-front">
    <div class="holder">
      <h1 class="holder-name">MARISOL VEGA, B.A.</h1>
      <p class="holder-role">Board Certified Asst. Behavior Analyst (BCABA)</p>
    </div>

    <div class="brand">
      <span class="brand-dot"></span>
      <span class="brand-name">KRT</span>
    </div>

    <div class="icon-tab">
      <svg viewBox="0 0 24 24" aria-label="Phone"><path fill="#fff" d="M3 9c0-3 4-5 9-5s9 2 9 5l-3 1-1-2H7L6 10 3 9zm4 1h10l2 9H5l2-9zm5 2a3 3 0 100 6 3 3 0 000-6z"/></svg>
      <svg viewBox="0 0 24 24" aria-label="Fax"><path fill="#fff" d="M7 2h8l3 3v5H7V2zm-3 9h16v8H4v-8zm3 5h10v6H7v-6zm2 2v1h6v-1H9z"/></svg>
      <svg viewBox="0 0 24 24" aria-label="Email"><path fill="none" stroke="#fff" stroke-width="2" d="M3 6h18v12H3zM3 6l9 7 9-7"/></svg>
      <svg viewBox="0 0 24 24" aria-label="Address"><path fill="#fff" d="M12 2a7 7 0 00-7 7c0 5 7 13 7 13s7-8 7-13a7 7 0 00-7-7zm0 4a3 3 0 110 6 3 3 0 010-6z"/></svg>
    </div>

    <ul class="contact">
      <li>07 41306152</li>
      <li>07 41306187</li>
      <li>info@krt.com</li>
      <li class="address">118 Harbour Lane<br>Coral Bay, Queensland 4710</li>
    </ul>

    <svg class="edge-bands" viewBox="0 0 620 44" preserveAspectRatio="none">
      <path fill="var(--brand-blue)" d="M0 36 L475 22 L475 44 L0 44 Z"/>
      <path fill="var(--leaf-green)" d="M458 44 L458 34 Q462 16 492 14 L620 10 L620 44 Z"/>
    </svg>
  </section>

</body>
</html>
```